Postcard Design

I need a postcard style insert designed that will be mailed out with a customer's monthly statement. This postcard will describe a new service offered to the customer by our company. The front of the postcard will have a design layout of the word definition for "Monetize" and similar to design layout used in a dictionary (i.e., enunciation, Verb, definition, and sample of how word is used). The backside of card will have brief description of service offered and contact information for my office.

Industry/Entity Type

It Company

```html
<!DOCTYPE html>
<html lang="en">
<head>
<meta charset="utf-8">
<title>Monetize Postcard</title>
<link rel="stylesheet" href="https://fonts.googleapis.com/css2?family=Questrial&family=Arimo:ital,wght@0,400;1,400&family=Source+Sans+3:wght@400;600&display=swap">
<style>
  :root {
    --stage: #333333;
    --navy: #1f1d45;
    --accent-red: #d6201f;
    --orange: #e57f00;
    --white: #ffffff;
    --wall: #cdd0c3;
    --page: #e4e6e8;
    --page-edge: #bdb6a4;
  }
  * { margin: 0; padding: 0; box-sizing: border-box; }
  html, body {
    width: 1200px; height: 652px; overflow: hidden;
    background: var(--stage);
  }
  .postcard {
    position: absolute; left: 123px; top: 142px;
    width: 953px; height: 366px;
    display: flex;
  }
  .front, .back { position: relative; height: 100%; }
  .front { width: 476px; }
  .back { width: 477px; background: var(--orange); }

  .front__photo {
    position: absolute; inset: 0;
    background:
      linear-gradient(90deg, rgba(40,30,20,0.55) 0 4px, transparent 4px) 56px 64px / 100% 100% no-repeat,
      linear-gradient(180deg, var(--wall) 0 58px, transparent 58px),
      linear-gradient(90deg, var(--wall) 0 55px, var(--page-edge) 55px 110px, var(--page) 140px, #eceef0 100%);
  }

  .entry { position: absolute; left: 161px; top: 112px; color: var(--navy); }
  .entry__word {
    font-family: "Questrial", sans-serif;
    font-size: 41px; font-weight: 400; letter-spacing: -0.5px; line-height: 1;
  }
  .entry__pronunciation {
    font-family: "Arimo", sans-serif;
    color: var(--accent-red); font-size: 12.5px; margin-top: 1px;
  }
  .entry__class {
    font-family: "Arimo", sans-serif; font-style: italic;
    color: var(--accent-red); font-size: 9.5px; margin-top: 8px;
  }
  .entry__senses {
    font-family: "Arimo", sans-serif; font-size: 9px; line-height: 11px;
    list-style: none; margin-top: 5px;
  }
  .entry__senses li { padding-left: 7px; text-indent: -7px; }

  .brand {
    position: absolute; display: flex; align-items: center; gap: 6px;
    font-family: "Arimo", sans-serif; color: var(--navy); font-weight: 400;
    white-space: nowrap;
  }
  .brand__dot { border-radius: 50%; background: var(--navy); flex: none; }
  .brand--front { left: 172px; top: 280px; font-size: 11px; }
  .brand--front .brand__dot { width: 10px; height: 10px; }
  .brand--back { left: 41px; top: 258px; font-size: 19px; }
  .brand--back .brand__dot { width: 16px; height: 16px; }

  .pitch {
    position: absolute; left: 34px; top: 37px;
    font-family: "Arimo", sans-serif; color: var(--white);
    font-size: 11px; line-height: 16.4px;
  }
  .privacy {
    position: absolute; left: 40px; top: 332px;
    font-family: "Source Sans 3", sans-serif; color: var(--navy);
    font-size: 8.3px; white-space: nowrap;
  }
</style>
</head>
<body>
  <main class="postcard">
    <section class="front">
      <div class="front__photo" role="img" aria-label="Photograph of an open dictionary with a ribbon bookmark against a pale wall"></div>
      <article class="entry">
        <h1 class="entry__word">mon·e·tize</h1>
        <p class="entry__pronunciation">/ˈmane.tiz/ &#128266;</p>
        <p class="entry__class">verb</p>
        <ol class="entry__senses">
          <li>1.Convert into or express in the form of currency.</li>
          <li>2.Convert real estate contract into currency that<br>&nbsp;&nbsp;an be used to purchase goods and services</li>
        </ol>
      </article>
      <div class="brand brand--front"><span class="brand__dot"></span>Hearthway Realty</div>
    </section>

    <section class="back">
      <p class="pitch">
        Interested in knowing what your<br>
        real estate contract is worth if you<br>
        were to sell it for a lump sum<br>
        cash payment?<br>
        Call Ledgerline Funding today<br>
        at 208-555-0142<br>
        for a free no-obligation quote<br>
        on the cash value of your contract.
      </p>
      <div class="brand brand--back"><span class="brand__dot"></span>Hearthway Realty</div>
      <p class="privacy">Your privacy is assured.&nbsp; Your escrow servicing providing this opportunity to you as a confidential courtesy</p>
    </section>
  </main>
</body>
</html>
```